Varenta Furniture Store needs an advertizing display

We just launched a furniture store in a place where not many people know us. So we need to display two vertical advertising banners (60cm x 160cm) to explain to the people our added value and our variety of products. We sell wooden furniture, chairs, upholstery, lamps and matresses. We diferenciate ourselves from the competition for our good quality and low prices. One banner needs to emphatize on our added value wich is "High end furniture at low prices". The other one needs to list our variety of products with prices starting at... Im uploading some images of the pieces we sell along with our logo.

Target Market(s)

People who want to improve their home decoration or who just moved to a new home

Industry/Entity Type

Furniture Store

Font styles to use
Sans Serif

Requirements
Must have
• One banner must have the look and feel of the brand (www.varenta-muebles.example) to comunicate our streghts which are high end products at affordable prices.
• The other one should have the variety of products we sell (wooden furniture, upholstery, matresses, lamps and chairs) with the lowest prices featured.

```html
<!DOCTYPE html>
<html lang="es">
<head>
<meta charset="utf-8">
<title>Varenta Furniture Store – Banner</title>
<link href="https://fonts.googleapis.com/css2?family=Roboto:ital,wght@0,500;0,700;1,700&family=Roboto+Condensed:wght@700&display=swap" rel="stylesheet">
<style>
  :root {
    --brand-green: #afd136;
    --ink-grey: #4b4b4d;
    --paper: #ffffff;
    --wall-light: #ecebea;
    --wall-grey: #c9c9c8;
    --wood-dark: #4a3a31;
    --wood-light: #d9c6a5;
    --fabric-grey: #a3a8aa;
    --floor-grey: #8c8884;
  }
  * { margin: 0; padding: 0; box-sizing: border-box; }
  html, body { width: 1200px; height: 3200px; overflow: hidden; background: var(--paper); }
  .banner { position: relative; width: 1200px; height: 3200px; background: var(--paper); font-family: "Roboto", Arial, sans-serif; }

  .top-band { position: absolute; left: 0; top: 0; width: 1200px; height: 22px; background: var(--brand-green); }
  .bottom-band { position: absolute; left: 0; top: 3160px; width: 1200px; height: 40px; background: var(--brand-green); }

  .hero-photo {
    position: absolute; left: 0; top: 22px; width: 1200px; height: 757px;
    background:
      linear-gradient(90deg, rgba(180,188,194,0.85) 0%, rgba(220,224,226,0.4) 22%, rgba(255,255,255,0) 40%),
      linear-gradient(180deg, var(--wall-light) 0%, #e2e1df 38%, #6a5a50 52%, var(--wood-dark) 62%, #9a948e 74%, var(--floor-grey) 100%);
  }

  .brand-tile {
    position: absolute; left: 419px; top: 667px; width: 362px; height: 368px;
    background: var(--brand-green);
    display: flex; align-items: center; justify-content: center;
  }
  .brand-name { color: var(--paper); font-weight: 700; font-size: 64px; letter-spacing: -0.5px; }

  .headline { position: absolute; left: 0; top: 1080px; width: 1200px; height: 680px; }
  .headline text { font-family: "Roboto Condensed", "Arial Narrow", sans-serif; font-weight: 700; }
  .headline .grey { fill: var(--ink-grey); }
  .headline .green { fill: var(--brand-green); }

  .photo-frame {
    position: absolute; border: 11px solid var(--brand-green); background: var(--paper); padding: 11px;
  }
  .photo-frame .photo { width: 100%; height: 100%; }
  .sofa-photo {
    background: linear-gradient(180deg, #f4f4f4 0%, #dfe1e2 30%, var(--fabric-grey) 48%, #8f9496 66%, #e9eaea 80%, #f7f7f7 100%);
  }
  .desk-photo {
    background:
      linear-gradient(90deg, rgba(150,160,168,0.7) 0%, rgba(255,255,255,0) 35%),
      linear-gradient(180deg, #dcdedf 0%, #eeeeec 40%, var(--wood-light) 55%, #e6ddcd 70%, #b4aea6 100%);
  }
  .bed-photo {
    background: linear-gradient(180deg, #ededeb 0%, #f4f3f1 35%, #e9e6e1 52%, #6a5446 64%, var(--wood-dark) 76%, #c9c3bb 90%, #d8d4cf 100%);
  }

  .price-tile {
    position: absolute; background: var(--brand-green);
    display: flex; align-items: center; justify-content: center;
  }
  .price-tile::after {
    content: ""; position: absolute; inset: 13px; border: 3px solid var(--paper);
  }
  .price-text { color: var(--paper); text-align: center; font-weight: 700; font-size: 40px; line-height: 1.18; }
  .price-text .from { font-style: italic; }
  .price-text .amount { font-size: 44px; }

  .site-url {
    position: absolute; left: 0; top: 2966px; width: 1200px; text-align: center;
    color: var(--ink-grey); font-weight: 700; font-size: 54px;
  }
</style>
</head>
<body>
<div class="banner">
  <div class="top-band"></div>
  <div class="hero-photo" role="img" aria-label="Sala moderna con mueble de TV de madera oscura, televisor y ventanal"></div>

  <div class="brand-tile"><span class="brand-name">Varenta</span></div>

  <svg class="headline" width="1200" height="680" viewBox="0 0 1200 680">
    <text class="grey" x="192" y="155" font-size="178" textLength="816" lengthAdjust="spacingAndGlyphs">MUEBLES</text>
    <text class="green" x="192" y="317" font-size="178" textLength="816" lengthAdjust="spacingAndGlyphs">DE LUJO A</text>
    <text class="grey" x="192" y="475" font-size="166" textLength="826" lengthAdjust="spacingAndGlyphs">LOS MEJORES</text>
    <text class="green" x="192" y="648" font-size="222" textLength="832" lengthAdjust="spacingAndGlyphs">PRECIOS</text>
  </svg>

  <div class="photo-frame" style="left:192px; top:1787px; width:509px; height:320px;">
    <div class="photo sofa-photo" role="img" aria-label="Sofá gris de tres plazas"></div>
  </div>
  <div class="price-tile" style="left:733px; top:1787px; width:275px; height:320px;">
    <p class="price-text">Sofás<br><span class="from">desde</span><br><span class="amount">$14,499</span></p>
  </div>

  <div class="price-tile" style="left:192px; top:2168px; width:277px; height:333px;">
    <p class="price-text">Escritorios<br><span class="from">desde</span><br><span class="amount">$2,895</span></p>
  </div>
  <div class="photo-frame" style="left:499px; top:2168px; width:509px; height:333px;">
    <div class="photo desk-photo" role="img" aria-label="Escritorio de madera clara con cajones blancos en oficina luminosa"></div>
  </div>

  <div class="photo-frame" style="left:192px; top:2547px; width:509px; height:333px;">
    <div class="photo bed-photo" role="img" aria-label="Cama matrimonial con base de madera oscura y colchón blanco"></div>
  </div>
  <div class="price-tile" style="left:733px; top:2547px; width:275px; height:333px;">
    <p class="price-text">Camas<br><span class="from">desde</span><br><span class="amount">$8,595</span></p>
  </div>

  <p class="site-url">www.varenta-muebles.example</p>
  <div class="bottom-band"></div>
</div>
</body>
</html>
```